Brimvane.com fiber optic internet website redesign

We need a new website design for our fiber optic internet company that provides internet, phone, and tv services. It should use the text "Marrowfen fiber optics", and "I beamed up with Marrowfen". The design should use the color blue and the attached logo.
We are a 30 year old internet company who started as a dial up internet provider in our basement. Today we design, build, and maintain our own fiber optic internet network to provide service to residential, business, educational, healthcare, and governmental customers

```html
<!DOCTYPE html>
<html lang="en">
<head>
<meta charset="utf-8">
<title>Brimvane.com – SOHO Internet – I beamed up with Marrowfen</title>
<link href="https://fonts.googleapis.com/css2?family=Kumbh+Sans:wght@500;700&family=Lato:wght@400;700&display=swap" rel="stylesheet">
<style>
:root{
  --blue:#0f55a8;
  --blue-bright:#1a6ad6;
  --navy:#0b1530;
  --night:#060c22;
  --red:#e3151b;
  --ink:#161616;
  --text:#2a2a2a;
  --line:#d5d9df;
  --white:#ffffff;
}
*{margin:0;padding:0;box-sizing:border-box}
html,body{width:1200px;height:2759px;overflow:hidden;background:var(--white)}
body{position:relative;font-family:"Lato",sans-serif;color:var(--text)}
.abs{position:absolute}
.display{font-family:"Kumbh Sans",sans-serif;font-weight:700;color:var(--ink)}

/* hero */
.hero{left:0;top:0;width:1200px;height:600px;overflow:hidden}
.hero-photo{position:absolute;inset:0;background:linear-gradient(120deg,#3a4660 0%,#1f2a48 45%,#141d38 100%)}
.hero-wave{position:absolute;left:0;top:0}
.brand{display:flex;align-items:center;gap:12px;color:var(--white)}
.brand-dot{border-radius:50%;background:var(--white);flex:none}
.brand-text{display:flex;flex-direction:column;align-items:flex-end}
.brand-name{font-family:"Kumbh Sans",sans-serif;font-weight:700;line-height:1}
.brand-sub{font-family:"Kumbh Sans",sans-serif;font-weight:700;line-height:1.1;margin-top:1px}
.top-phone{left:796px;top:14px;color:var(--white);font-size:16px;font-weight:700}
.btn-top{top:6px;height:37px;display:flex;align-items:center;justify-content:center;font-size:14px;font-weight:700}
.btn-user{left:936px;width:91px;background:var(--white);color:var(--ink)}
.btn-support{left:1034px;width:100px;background:var(--blue-bright);color:var(--white)}
.nav{top:57px;left:344px;display:flex;color:var(--white);font-size:16px;font-weight:700}
.nav span{margin-right:50px}
.nav span:last-child{margin-right:0}
.nav .active{color:var(--red)}
.hero-kicker{left:0;width:1200px;text-align:center;top:186px;font-size:33px;color:var(--white);font-family:"Kumbh Sans",sans-serif;font-weight:700}
.hero-title{left:0;width:1200px;text-align:center;top:228px;font-size:58px;color:var(--white);font-family:"Kumbh Sans",sans-serif;font-weight:700}
.crumbs{left:0;width:1200px;text-align:center;top:322px;font-size:14px;color:var(--white)}
.crumbs em{font-style:normal;color:var(--red)}

/* pricing */
.pricing-title{left:63px;top:608px;font-size:47px;line-height:55px}
.pricing-lede{left:66px;top:733px;width:805px;font-size:17px;line-height:26px}
.plans{left:66px;top:820px;width:1068px;border-collapse:separate;border-spacing:2px;font-size:14px;color:var(--ink);margin-left:-2px}
.plans th{background:var(--blue);color:var(--white);height:44px;font-size:16px;font-weight:700;width:20%}
.plans td{height:46px;text-align:center;border:1px solid var(--line)}
.plans td.pkg{background:var(--blue);color:var(--white);border-color:var(--blue)}
.plans a{color:var(--red);text-decoration:underline}
.promo{left:67px;top:1206px;width:1070px;font-size:16px;line-height:26px;color:var(--red)}

/* includes */
.includes-title{left:63px;top:1343px;font-size:47px}
.features{left:66px;top:1433px;width:630px;list-style:none;font-size:16px;line-height:22px;color:var(--ink)}
.features li{display:flex;gap:8px;margin-bottom:18px}
.features svg{flex:none;margin-top:6px}
.includes-photo{left:717px;top:1353px;width:416px;height:487px;background:linear-gradient(160deg,#c9b9a8 0%,#8f7f74 45%,#5c5058 100%)}

.voip{left:0;width:1200px;text-align:center;top:1903px;font-size:40px;font-family:"Kumbh Sans",sans-serif;font-weight:500;color:#222}
.voip b{color:var(--blue);font-weight:700}
.cta{left:486px;top:1970px;width:228px;height:49px;background:var(--blue);color:var(--white);font-size:15px;font-weight:700;display:flex;align-items:center;justify-content:center}

/* footer */
.footer-bg{left:0;top:2040px}
.footer-tag{left:66px;top:2432px;width:380px;font-size:15px;line-height:22px;color:#e6e9f2}
.social{top:2508px;width:38px;height:38px;background:#1c2440;border:1px solid #2c3658;display:flex;align-items:center;justify-content:center}
.col-title{top:2334px;font-size:21px;color:var(--white);font-family:"Kumbh Sans",sans-serif;font-weight:700}
.quick{left:489px;top:2378px;list-style:none;font-size:14px;color:#e6e9f2;line-height:32px}
.contact-row{left:691px;display:flex;align-items:flex-start;gap:10px;font-size:14px;color:#e6e9f2;line-height:20px}
.contact-ico{width:36px;height:36px;border-radius:50%;background:var(--blue);display:flex;align-items:center;justify-content:center;flex:none}
.support-row{left:969px;display:flex;align-items:center;gap:7px;font-size:14px;color:#e6e9f2}
.rule{left:66px;top:2700px;width:1068px;height:1px;background:#2a3352}
.legal{left:66px;top:2723px;font-size:10px;letter-spacing:1px;color:#b6bccb}
.copyright{left:0;width:1200px;text-align:center;top:2722px;font-size:12px;color:#c7ccd9}
.copyright em{font-style:normal;color:var(--red)}
</style>
</head>
<body>

<header class="abs hero">
  <div class="hero-photo" role="img" aria-label="Businessman in a suit on a phone call with a laptop in a city plaza"></div>
  <svg class="hero-wave" width="1200" height="600" viewBox="0 0 1200 600" aria-hidden="true">
    <path d="M0,440 C70,360 160,325 230,330 C350,338 450,450 570,525 C690,598 800,602 910,560 C1040,510 1140,440 1200,365 L1200,600 L0,600 Z" fill="var(--blue-bright)"/>
    <path d="M0,458 C70,380 160,342 230,347 C350,355 450,465 570,540 C690,608 790,594 900,558 C1020,515 1130,460 1200,400 L1200,600 L0,600 Z" fill="#ffffff"/>
  </svg>
</header>

<div class="abs brand" style="left:66px;top:48px">
  <span class="brand-dot" style="width:42px;height:42px"></span>
  <span class="brand-text">
    <span class="brand-name" style="font-size:23px">Brimvane.com</span>
    <span class="brand-sub" style="font-size:10px">Marrowfen Fiber Optics</span>
  </span>
</div>
<div class="abs top-phone">1-888-555-0142</div>
<div class="abs btn-top btn-user">USER</div>
<div class="abs btn-top btn-support">SUPPORT</div>
<nav class="abs nav">
  <span>HOME</span><span>RESIDENTIAL</span><span class="active">BUSINESS</span><span>SERVICES</span><span>FAQ</span><span>TELECOM</span><span>CONTACT US</span>
</nav>
<div class="abs hero-kicker">Business</div>
<h1 class="abs hero-title">SOHO Internet</h1>
<div class="abs crumbs">Home &gt; Business &gt; <em>SOHO Internet</em></div>

<h2 class="abs display pricing-title">SOHO/Business Internet<br>Pricing Plans up to 1 Gigabit !!!</h2>
<p class="abs pricing-lede">Speeds up to 10Gb symmetrical are available. If you don't see what package you are looking for please contact us for pricing.</p>

<table class="abs plans">
  <thead><tr><th>PACKAGE</th><th>DOWNLOAD SPEED</th><th>UPLOAD SPEED</th><th>DATA TRANSFER</th><th>MONTHLY PRICE</th></tr></thead>
  <tbody>
    <tr><td class="pkg">25MB</td><td>25 MBPS</td><td>10 MBPS</td><td>2000 GigaBytes</td><td>Call or <a>Email</a> for a Quote</td></tr>
    <tr><td class="pkg">50MB</td><td>50 MBPS</td><td>15 MBPS</td><td>2000 GigaBytes</td><td>Call or <a>Email</a> for a Quote</td></tr>
    <tr><td class="pkg">75MB</td><td>75 MBPS</td><td>20 MBPS</td><td>2000 GigaBytes</td><td>Call or <a>Email</a> for a Quote</td></tr>
    <tr><td class="pkg">100MB</td><td>100 MBPS</td><td>25 MBPS</td><td>3000 GigaBytes</td><td>Call or <a>Email</a> for a Quote</td></tr>
    <tr><td class="pkg">200MB</td><td>200 MBPS</td><td>50 MBPS</td><td>3000 GigaBytes</td><td>Call or <a>Email</a> for a Quote</td></tr>
    <tr><td class="pkg">500MB</td><td>500 MBPS</td><td>75 MBPS</td><td>4000 GigaBytes</td><td>Call or <a>Email</a> for a Quote</td></tr>
    <tr><td class="pkg">1000MB</td><td>1000 MBPS</td><td>100 MBPS</td><td>5000 GigaBytes</td><td>Call or <a>Email</a> for a Quote</td></tr>
  </tbody>
</table>
<p class="abs promo">Need Fast and Reliable Service? Fill out this Form to see what DISCOUNTS are available in your area. For a competitive quote send us a copy of your current bill to sales@marrowfen.com or fax us at 724-555-0167.</p>

<h2 class="abs display includes-title">Internet Service Includes</h2>
<ul class="abs features">
  <li><svg width="13" height="11" viewBox="0 0 13 11"><path d="M1 6l4 4 7-9" fill="none" stroke="var(--blue)" stroke-width="2.6"/></svg>High Speed Fiber Optic Internet Connection</li>
  <li><svg width="13" height="11" viewBox="0 0 13 11"><path d="M1 6l4 4 7-9" fill="none" stroke="var(--blue)" stroke-width="2.6"/></svg>Static IP Addressing</li>
  <li><svg width="13" height="11" viewBox="0 0 13 11"><path d="M1 6l4 4 7-9" fill="none" stroke="var(--blue)" stroke-width="2.6"/></svg>Free Email Addresses</li>
  <li><svg width="13" height="11" viewBox="0 0 13 11"><path d="M1 6l4 4 7-9" fill="none" stroke="var(--blue)" stroke-width="2.6"/></svg>Unlimited file size on email attachments</li>
  <li><svg width="13" height="11" viewBox="0 0 13 11"><path d="M1 6l4 4 7-9" fill="none" stroke="var(--blue)" stroke-width="2.6"/></svg>Fast and Friendly LOCAL Phone Support</li>
  <li><svg width="13" height="11" viewBox="0 0 13 11"><path d="M1 6l4 4 7-9" fill="none" stroke="var(--blue)" stroke-width="2.6"/></svg>Discounted Computer Repair Services</li>
  <li><svg width="13" height="11" viewBox="0 0 13 11"><path d="M1 6l4 4 7-9" fill="none" stroke="var(--blue)" stroke-width="2.6"/></svg>Free installation and setup</li>
  <li><svg width="13" height="11" viewBox="0 0 13 11"><path d="M1 6l4 4 7-9" fill="none" stroke="var(--blue)" stroke-width="2.6"/></svg>Price does not include applicable franchise fees or taxes</li>
  <li><svg width="13" height="11" viewBox="0 0 13 11"><path d="M1 6l4 4 7-9" fill="none" stroke="var(--blue)" stroke-width="2.6"/></svg>If you need more bandwidth you can upgrade at any time!</li>
  <li><svg width="13" height="11" viewBox="0 0 13 11"><path d="M1 6l4 4 7-9" fill="none" stroke="var(--blue)" stroke-width="2.6"/></svg>The bandwidth limits are not data capped and we will not slow you down or stop your connection if you exceed these limits.</li>
</ul>
<div class="abs includes-photo" role="img" aria-label="Young woman in a patterned bucket hat using a laptop on a train platform"></div>

<div class="abs voip">Add VoIP Phone Service for <b>$25/Line</b></div>
<div class="abs cta">CHECK AVAILABILITY</div>

<svg class="abs footer-bg" width="1200" height="719" viewBox="0 0 1200 719" aria-hidden="true">
  <defs>
    <linearGradient id="footShade" x1="0" y1="0" x2="1" y2="1">
      <stop offset="0" stop-color="#0a1430"/>
      <stop offset="0.5" stop-color="#0c1436"/>
      <stop offset="1" stop-color="#050a1c"/>
    </linearGradient>
  </defs>
  <path d="M0,222 C110,90 280,10 410,12 C560,14 660,140 780,215 C880,275 960,272 1040,240 C1110,212 1160,185 1200,165 L1200,719 L0,719 Z" fill="url(#footShade)"/>
</svg>

<div class="abs brand" style="left:66px;top:2340px">
  <span class="brand-dot" style="width:62px;height:62px"></span>
  <span class="brand-text">
    <span class="brand-name" style="font-size:34px">Brimvane.com</span>
    <span class="brand-sub" style="font-size:14px">Marrowfen Fiber Optics</span>
  </span>
</div>
<p class="abs footer-tag">Fiber optic-based communications have been used for years by government and industry.</p>
<div class="abs social" style="left:66px" aria-label="Social profile 1"><svg width="10" height="10"><rect width="10" height="10" fill="#fff"/></svg></div>
<div class="abs social" style="left:120px" aria-label="Social profile 2"><svg width="10" height="10"><rect width="10" height="10" fill="#fff"/></svg></div>
<div class="abs social" style="left:174px" aria-label="Social profile 3"><svg width="10" height="10"><rect width="10" height="10" fill="#fff"/></svg></div>

<div class="abs col-title" style="left:488px">Quick Links</div>
<ul class="abs quick">
  <li>Home</li><li>Residential</li><li>Business</li><li>Services</li><li>FAQ</li><li>Telecom</li><li>Contact us</li><li>Users</li><li>Support</li>
</ul>

<div class="abs col-title" style="left:691px">Contact Us</div>
<div class="abs contact-row" style="top:2378px">
  <span class="contact-ico"><svg width="12" height="16" viewBox="0 0 12 16"><path d="M6 0a6 6 0 0 0-6 6c0 4 6 10 6 10s6-6 6-10a6 6 0 0 0-6-6z" fill="#fff"/><circle cx="6" cy="6" r="2.2" fill="var(--blue)"/></svg></span>
  <span style="padding-top:2px">118 Alder Street Kellsport,<br>PA 16000</span>
</div>
<div class="abs contact-row" style="top:2436px;align-items:center">
  <span class="contact-ico"><svg width="14" height="14" viewBox="0 0 14 14"><path d="M3 0l3 3-2 2a8 8 0 0 0 5 5l2-2 3 3-2 3C6 14 0 8 0 2z" fill="#fff"/></svg></span>
  <span>724-555-0193</span>
</div>
<div class="abs contact-row" style="top:2490px;align-items:center">
  <span class="contact-ico"><svg width="16" height="12" viewBox="0 0 16 12"><rect x="1" y="1" width="14" height="10" fill="none" stroke="#fff" stroke-width="1.6"/><path d="M1 1l7 6 7-6" fill="none" stroke="#fff" stroke-width="1.6"/></svg></span>
  <span>sales@marrowfen.com</span>
</div>

<div class="abs col-title" style="left:969px">Support</div>
<div class="abs support-row" style="top:2380px">
  <svg width="13" height="13" viewBox="0 0 14 14"><path d="M3 0l3 3-2 2a8 8 0 0 0 5 5l2-2 3 3-2 3C6 14 0 8 0 2z" fill="#fff"/></svg>1-888-555-0142
</div>
<div class="abs support-row" style="top:2424px">
  <svg width="15" height="11" viewBox="0 0 16 12"><rect x="1" y="1" width="14" height="10" fill="none" stroke="#fff" stroke-width="1.6"/><path d="M1 1l7 6 7-6" fill="none" stroke="#fff" stroke-width="1.6"/></svg>support@marrowfen.com
</div>

<div class="abs rule"></div>
<div class="abs legal">PRIVACY POLICY | TERMS OF CONDITION</div>
<div class="abs copyright">© <em>BRIMVANE</em>, 2024. ALL RIGHTS RESERVED.</div>

</body>
</html>
```